Intermodal Trucking Company Website

My client is a trucking company that takes the containers you see on the back of a ship or railroad car and delivers them in the midwestern part of the United States. Here are some of their competitors Websites and their logo to use as part of the design.

http://www.varnekhaulers.example/
https://www.plirext.example/
http://www.brontagefreight.example/
https://www.lqp-xy.example/

Industry/Entity Type

Trucking Company

Number of Pages Required

2 page

Requirements
Must have
• Website must be professional and the design needs to be suitable for a responsive Website.
Should not have
• Please do not submit designs with misspellings. Designs with misspellings will be eliminated.

```html
<!DOCTYPE html>
<html lang="en">
<head>
<meta charset="utf-8">
<title>Keltarro Intermodal</title>
<link href="https://fonts.googleapis.com/css2?family=Roboto+Condensed:wght@300;400;700&family=Open+Sans:wght@400;600&display=swap" rel="stylesheet">
<style>
:root{
  --accent:#e5533b;
  --accent-dark:#c9432d;
  --ink:#2c2c2c;
  --muted:#8a8a8a;
  --line:#e2e2e2;
  --page:#ffffff;
  --soft:#ededed;
  --footer:#2e2e2e;
  --footer-bar:#232323;
  --footer-text:#a9a9a9;
}
*{box-sizing:border-box;margin:0;padding:0}
html,body{width:1200px;height:3108px;overflow:hidden;background:var(--page)}
body{font-family:"Open Sans",Arial,sans-serif;color:var(--ink);font-size:12px;line-height:1.6}

/* header */
.site-header{height:96px;position:relative;border-bottom:1px solid var(--line)}
.brand{position:absolute;left:148px;top:16px;display:flex;align-items:center;gap:10px}
.brand-mark{width:22px;height:22px;border-radius:50%;background:var(--accent)}
.brand-name{font-family:"Roboto Condensed",sans-serif;font-weight:700;font-size:18px;color:var(--ink);line-height:1.1;width:130px}
.top-contact{position:absolute;left:420px;top:8px;display:flex;gap:30px;font-size:11px;color:var(--muted)}
.top-contact span{display:flex;align-items:center;gap:6px}
.main-nav{position:absolute;left:470px;top:48px;display:flex;gap:26px;font-family:"Roboto Condensed",sans-serif;font-size:12px;font-weight:700;text-transform:uppercase;white-space:nowrap}
.main-nav a{color:var(--ink);text-decoration:none;padding-bottom:6px}
.main-nav a.active{color:var(--accent);border-bottom:2px solid var(--accent)}
.search-btn{position:absolute;left:1020px;top:42px;width:30px;height:30px;background:var(--accent);display:flex;align-items:center;justify-content:center}

/* hero */
.hero{height:584px;position:relative;overflow:hidden}
.hero-photo{position:absolute;inset:0;background:linear-gradient(180deg,#2a2420 0%,#5b3f2c 40%,#8a5a38 65%,#3a2a22 100%)}
.hero-content{position:absolute;left:0;right:0;top:150px;text-align:center;color:#fff}
.hero h1{font-family:"Roboto Condensed",sans-serif;font-weight:700;font-size:46px;line-height:1.05;text-transform:uppercase}
.hero h1 .accent{display:block;color:var(--accent)}
.hero p{width:420px;margin:20px auto 0;font-size:12px;color:#e9e1d9}
.btn{display:inline-block;background:var(--accent);color:#fff;font-family:"Roboto Condensed",sans-serif;font-weight:700;font-size:13px;text-transform:uppercase;padding:10px 26px}
.hero .btn{margin-top:26px}
.hero-arrow{position:absolute;top:375px;width:28px;height:34px;background:rgba(255,255,255,.9);display:flex;align-items:center;justify-content:center}
.hero-arrow.prev{left:0}.hero-arrow.next{right:0}
.hero-dots{position:absolute;bottom:30px;left:0;right:0;display:flex;justify-content:center;gap:8px}
.hero-dots i{width:8px;height:8px;border-radius:50%;background:#fff;opacity:.6}
.hero-dots i.on{background:var(--accent);opacity:1}

/* about */
.about{height:300px;position:relative}
.about-photo{position:absolute;left:170px;top:90px;width:400px;height:140px;background:linear-gradient(90deg,#e27a36,#d96a2b 50%,#e8a63a);border-radius:4px}
.about-text{position:absolute;left:610px;top:100px;width:430px}
.about-text h3{font-family:"Roboto Condensed",sans-serif;font-weight:700;font-size:15px;text-transform:uppercase;line-height:1.3}
.about-text p{margin-top:12px;font-size:11px;color:var(--muted);line-height:1.7}

/* section titles */
.section-title{text-align:center}
.section-title h2{font-family:"Roboto Condensed",sans-serif;font-weight:300;font-size:30px;text-transform:uppercase;letter-spacing:.5px;color:var(--ink)}
.section-title h2 b{color:var(--accent);font-weight:400}
.section-title .rule{display:block;margin:6px auto 0}
.section-title p{width:360px;margin:14px auto 0;font-size:10px;color:var(--muted);text-transform:uppercase;line-height:1.6}

/* services */
.services{height:520px;position:relative;padding-top:20px}
.service-grid{position:absolute;left:160px;top:150px;width:880px;display:grid;grid-template-columns:repeat(3,282px);column-gap:17px;row-gap:40px}
.service-card{height:120px;border:1px solid var(--line);display:flex;align-items:center;gap:18px;box-shadow:0 2px 4px rgba(0,0,0,.04)}
.service-num{width:60px;height:60px;background:var(--accent);color:#fff;font-family:"Roboto Condensed",sans-serif;font-weight:700;font-size:36px;display:flex;align-items:center;justify-content:center;margin-left:-1px}
.service-card h4{font-family:"Roboto Condensed",sans-serif;font-weight:700;font-size:14px;line-height:1.2;text-transform:uppercase;width:170px}

/* why */
.why-title{height:150px;padding-top:12px}
.why-band{height:380px;display:flex}
.why-photo{width:600px;background:linear-gradient(180deg,#f1f1f1,#dcdcdc 60%,#cfcfcf)}
.why-list{width:600px;background:var(--accent);padding:50px 0 0 0;color:#fff}
.why-item{display:flex;gap:24px;margin-bottom:44px}
.why-num{width:46px;height:46px;flex:none;background:#fff;color:var(--accent);font-family:"Roboto Condensed",sans-serif;font-weight:700;font-size:22px;display:flex;align-items:center;justify-content:center;margin-left:-23px}
.why-item h5{font-family:"Roboto Condensed",sans-serif;font-weight:700;font-size:13px;text-transform:uppercase}
.why-item p{font-size:10px;width:440px;line-height:1.6;opacity:.92}

/* quote */
.quote{height:510px;position:relative;padding-top:110px}
.quote-form{position:absolute;left:160px;top:230px;width:880px}
.field-row{display:grid;grid-template-columns:repeat(4,1fr);gap:16px}
.field{height:34px;border:1px solid var(--line);font-size:10px;color:var(--muted);padding:9px 10px}
.field.message{height:122px;margin-top:26px}
.quote-form .btn{display:block;width:120px;margin:34px auto 0;text-align:center;padding:9px 0;font-size:11px}

/* clients */
.clients{height:272px;position:relative}
.client-row{position:absolute;left:160px;top:196px;width:880px;display:flex;justify-content:space-around}
.client-name{font-family:"Roboto Condensed",sans-serif;font-weight:700;font-size:28px;color:#3a3a3a}

/* footer */
.site-footer{height:296px;background:var(--footer);color:var(--footer-text);position:relative}
.footer-main{height:256px;position:relative}
.footer-about{position:absolute;left:160px;top:32px;width:240px}
.footer-brand{display:flex;align-items:center;gap:8px;font-family:"Roboto Condensed",sans-serif;font-weight:700;font-size:16px;color:#fff}
.footer-brand i{width:18px;height:18px;border-radius:50%;background:var(--accent)}
.footer-about p{margin-top:14px;font-size:10px;line-height:1.7}
.footer-col{position:absolute;top:40px;font-size:10px}
.footer-col h6{font-family:"Roboto Condensed",sans-serif;font-size:12px;color:#fff;text-transform:uppercase;margin-bottom:10px}
.footer-col ul{list-style:none;line-height:2.3}
.footer-col.links-a{left:460px}.footer-col.links-b{left:600px;top:68px}
.footer-col.contact{left:760px;width:280px}
.footer-col.contact p{line-height:1.7}
.subscribe{margin-top:16px;height:30px;border:1px solid #555;display:flex;align-items:center;justify-content:space-between;padding:0 10px;color:#888}
.footer-bar{height:40px;background:var(--footer-bar);text-align:center;font-size:10px;line-height:40px;color:#8c8c8c}
</style>
</head>
<body>

<header class="site-header">
  <div class="brand"><span class="brand-mark"></span><span class="brand-name">Keltarro Intermodal</span></div>
  <div class="top-contact">
    <span><svg width="10" height="10" viewBox="0 0 10 10"><path d="M2 1l2 2-1 1.5a6 6 0 0 0 2.5 2.5L7 6l2 2-1.5 1.5C4 9 1 6 .5 2.5z" fill="#e5533b"/></svg>(555) 014-2280</span>
    <span><svg width="11" height="9" viewBox="0 0 11 9"><rect x=".5" y=".5" width="10" height="8" fill="none" stroke="#e5533b"/><path d="M.5.5l5 4 5-4" fill="none" stroke="#e5533b"/></svg>info@keltarro.example</span>
  </div>
  <nav class="main-nav">
    <a class="active" href="#">Home</a><a href="#">About</a><a href="#">Services</a><a href="#">Freight &amp; Trucks</a><a href="#">News &amp; Events</a><a href="#">Contact</a>
  </nav>
  <div class="search-btn"><svg width="13" height="13" viewBox="0 0 13 13"><circle cx="5.5" cy="5.5" r="4" fill="none" stroke="#fff" stroke-width="1.6"/><path d="M8.5 8.5l3.5 3.5" stroke="#fff" stroke-width="1.6"/></svg></div>
</header>

<section class="hero">
  <div class="hero-photo" role="img" aria-label="Red semi truck on a desert highway at sunset"></div>
  <div class="hero-content">
    <h1>Nam elementum porttitor <span class="accent">erat et elementum</span></h1>
    <p>Ut hac habitasse platea dictumst. Nam tellus massa, aliquet et tincidunt sit amet, pellentesque quis diam. Fusce viverra posuere et libero ac vestibulum tempor.</p>
    <span class="btn">Request a free quote &nbsp;›</span>
  </div>
  <div class="hero-arrow prev"><svg width="8" height="12" viewBox="0 0 8 12"><path d="M6 1L1 6l5 5" fill="none" stroke="#333" stroke-width="2"/></svg></div>
  <div class="hero-arrow next"><svg width="8" height="12" viewBox="0 0 8 12"><path d="M2 1l5 5-5 5" fill="none" stroke="#333" stroke-width="2"/></svg></div>
  <div class="hero-dots"><i></i><i class="on"></i><i></i></div>
</section>

<section class="about">
  <div class="about-photo" role="img" aria-label="Three colourful semi trucks parked side by side"></div>
  <div class="about-text">
    <h3>Curabitur sollicitudin est augue,<br>a auctor risus luctus vel</h3>
    <p>In hac habitasse platea dictumst. Nam tellus massa, aliquet et tincidunt sit amet, pellentesque quis diam. Curabitur in porta metus, sed dictum urna. Vivamus vitae nibh nec ipsum dapibus pretium. Nulla facilisi. Integer tempor sem eget lorem vulputate, vitae varius magna gravida. Donec non orci a metus aliquam facilisis. Phasellus posuere, risus vel ultrices bibendum, mauris lacus fermentum nisl, at luctus lorem magna id justo.</p>
  </div>
</section>

<section class="services">
  <div class="section-title">
    <h2>Our <b>Services</b></h2>
    <svg class="rule" width="24" height="10" viewBox="0 0 24 10"><rect x="2" y="2" width="12" height="5" fill="#e5533b"/><rect x="14" y="4" width="6" height="3" fill="#e5533b"/><circle cx="6" cy="8.5" r="1.5" fill="#2c2c2c"/><circle cx="17" cy="8.5" r="1.5" fill="#2c2c2c"/></svg>
    <p>We have wide network of offices in all major locations to help you with the services we offer</p>
  </div>
  <div class="service-grid">
    <div class="service-card"><span class="service-num">1</span><h4>There are many variations of passages of</h4></div>
    <div class="service-card"><span class="service-num">2</span><h4>There are many variations of passages of</h4></div>
    <div class="service-card"><span class="service-num">3</span><h4>There are many variations of passages of</h4></div>
    <div class="service-card"><span class="service-num">4</span><h4>There are many variations of passages of</h4></div>
    <div class="service-card"><span class="service-num">5</span><h4>There are many variations of passages of</h4></div>
    <div class="service-card"><span class="service-num">6</span><h4>There are many variations of passages of</h4></div>
  </div>
</section>

<section class="why">
  <div class="why-title section-title">
    <h2>Why <b>Choose Us</b></h2>
    <svg class="rule" width="24" height="10" viewBox="0 0 24 10"><rect x="2" y="2" width="12" height="5" fill="#e5533b"/><rect x="14" y="4" width="6" height="3" fill="#e5533b"/><circle cx="6" cy="8.5" r="1.5" fill="#2c2c2c"/><circle cx="17" cy="8.5" r="1.5" fill="#2c2c2c"/></svg>
    <p>We have wide network of offices in all major locations to help you with the services we offer</p>
  </div>
  <div class="why-band">
    <div class="why-photo" role="img" aria-label="White semi truck with trailer on a light grey background"></div>
    <div class="why-list">
      <div class="why-item"><span class="why-num">1</span><div><h5>Fusce iaculis dolor ut pharetra ultrices</h5><p>Vestibulum ante ipsum primis in faucibus orci luctus et ultrices posuere cubilia curae. Sed pulvinar nisi quis lacus placerat, at feugiat nisl tempus. Mauris ut lectus id diam.</p></div></div>
      <div class="why-item"><span class="why-num">2</span><div><h5>Fusce iaculis dolor ut pharetra ultrices</h5><p>Vestibulum ante ipsum primis in faucibus orci luctus et ultrices posuere cubilia curae. Sed pulvinar nisi quis lacus placerat, at feugiat nisl tempus. Mauris ut lectus id diam.</p></div></div>
      <div class="why-item"><span class="why-num">3</span><div><h5>Fusce iaculis dolor ut pharetra ultrices</h5><p>Vestibulum ante ipsum primis in faucibus orci luctus et ultrices posuere cubilia curae. Sed pulvinar nisi quis lacus placerat, at feugiat nisl tempus. Mauris ut lectus id diam.</p></div></div>
    </div>
  </div>
</section>

<section class="quote">
  <div class="section-title">
    <h2>Get a <b>Quote</b></h2>
    <svg class="rule" width="24" height="10" viewBox="0 0 24 10"><rect x="2" y="2" width="12" height="5" fill="#e5533b"/><rect x="14" y="4" width="6" height="3" fill="#e5533b"/><circle cx="6" cy="8.5" r="1.5" fill="#2c2c2c"/><circle cx="17" cy="8.5" r="1.5" fill="#2c2c2c"/></svg>
    <p>We have wide network of offices in all major locations to help you with the services we offer</p>
  </div>
  <div class="quote-form">
    <div class="field-row">
      <div class="field">Full Name</div><div class="field">Company Name</div><div class="field">Phone</div><div class="field">Email</div>
    </div>
    <div class="field message">Message</div>
    <span class="btn">Get a Quote</span>
  </div>
</section>

<section class="clients">
  <div class="section-title">
    <h2>Our <b>Clients</b></h2>
    <svg class="rule" width="24" height="10" viewBox="0 0 24 10"><rect x="2" y="2" width="12" height="5" fill="#e5533b"/><rect x="14" y="4" width="6" height="3" fill="#e5533b"/><circle cx="6" cy="8.5" r="1.5" fill="#2c2c2c"/><circle cx="17" cy="8.5" r="1.5" fill="#2c2c2c"/></svg>
    <p>We have wide network of offices in all major locations to help you with the services we offer</p>
  </div>
  <div class="client-row">
    <span class="client-name">Norvane</span><span class="client-name">Brontage</span><span class="client-name">Plirext</span><span class="client-name">Varnek</span>
  </div>
</section>

<footer class="site-footer">
  <div class="footer-main">
    <div class="footer-about">
      <div class="footer-brand"><i></i>Keltarro Intermodal</div>
      <p>Container drayage from rail yards and ports across the Midwest. Safe, on time and fully tracked from pickup to delivery, with drivers who know every route.</p>
    </div>
    <div class="footer-col links-a">
      <h6>Quick Links</h6>
      <ul><li>About Us</li><li>Services</li><li>Our Fleet</li><li>News</li><li>Careers</li></ul>
    </div>
    <div class="footer-col links-b">
      <ul><li>Drayage</li><li>Storage</li><li>Tracking</li><li>Safety</li><li>Contact</li></ul>
    </div>
    <div class="footer-col contact">
      <h6>Quick Links</h6>
      <p>Sign up for our news and updates. Get notified about new routes and service changes across our network.</p>
      <div class="subscribe">Email Address<svg width="12" height="10" viewBox="0 0 12 10"><path d="M0 5l12-5-3 10-3-4z" fill="#bbb"/></svg></div>
    </div>
  </div>
  <div class="footer-bar">Copyright 2024 Keltarro Intermodal. All rights reserved.</div>
</footer>

</body>
</html>
```